Corvane Hollis Landing Page

We need a landing page re-designed for a new website www.corvanehollis.com and the website is live if you search the address provided.
We need the industry standard files for embedding this into the landing page of our website. The company is a real estate advisory firm, we provide professional property services and are focused on business rates (commercial property taxation in the UK).
We have uploaded a file which is meant to provide a visual guide as to how we envisage the landing page looking. You are free to come up with an entirely different creative design. The image at the top with the search button is taken from another website so the design will need to be distinctly different but may follow the same theme. Furthermore, the colour palette does not need to be followed slavishly and can be modified changed and improved upon. It might be that you want to incorporate other visual cues such as a desktop PC, laptop and Vexa as these are devices the website will be accessed from; however, this is not essential and only a guide.
**To clarify, please note, the target industry is commercial properties and not residential or domestic property, so please when incorporating designs of buildings its important to focus on commercial property such as shops, offices, industrial buildings etc.**
Occupiers of commercial real estate in the UK who pay property tax to occupy the property.

```html
<!DOCTYPE html>
<html lang="en">
<head>
<meta charset="utf-8">
<title>Corvane Hollis</title>
<link rel="stylesheet" href="https://fonts.googleapis.com/css2?family=Roboto:wght@300;400;500&family=Roboto+Condensed:wght@400&family=Open+Sans:ital,wght@0,400;1,400&display=swap">
<style>
:root{
  --orange:#f47a20;
  --ink:#1c1c1c;
  --muted:#555;
  --white:#fff;
  --field:#e8e8e8;
  --sky-top:#7f93a6;
  --sky-bottom:#5d5a55;
  --steel-dark:#2b2b2b;
  --steel-light:#8a8a8a;
}
*{margin:0;padding:0;box-sizing:border-box}
html,body{width:1200px;height:2276px;overflow:hidden;background:var(--white)}
body{position:relative;font-family:"Roboto",sans-serif;color:var(--ink)}
.abs{position:absolute}
.hero-photo,.band-photo{position:absolute;left:0;width:1200px}
.hero-photo{top:0;height:751px;background:linear-gradient(180deg,var(--sky-top) 0%,#8c98a2 35%,#6d6b66 70%,var(--sky-bottom) 100%);clip-path:polygon(0 0,100% 0,100% 751px,0 680px)}
.band-photo{top:1195px;height:580px;background:linear-gradient(160deg,#505050 0%,#8f8f8f 30%,#3a3a3a 60%,#6e6e6e 80%,var(--steel-dark) 100%);clip-path:polygon(0 0,100% 78px,100% 580px,0 519px)}
.brand{display:flex;align-items:center;gap:10px;font-family:"Roboto",sans-serif;font-weight:500;letter-spacing:1px}
.brand-mark{width:14px;height:14px;background:var(--orange)}
.brand.header{left:78px;top:40px;font-size:18px;color:var(--white)}
.brand.header .brand-mark{background:var(--white)}
.nav{top:46px;font-size:12.5px;font-weight:500;color:var(--white)}
.pill{border-radius:20px;font-size:10.5px;font-weight:500;display:flex;align-items:center;justify-content:center;height:30px;width:82px;top:37px}
.pill.login{left:948px;border:2px solid var(--white);color:var(--white)}
.pill.register{left:1043px;background:var(--white);color:#777}
.hero-title{left:75px;top:150px;font-size:58px;font-weight:400;line-height:76px;color:var(--white);text-transform:uppercase}
.hero-text{left:75px;top:406px;font-size:17.5px;line-height:24px;color:var(--white);width:680px}
.btn{background:var(--orange);color:var(--white);border-radius:30px;display:flex;align-items:center;justify-content:center;text-transform:uppercase;font-family:"Roboto Condensed",sans-serif}
.btn.hero-cta{left:75px;top:505px;width:250px;height:50px;font-size:17px}
.brand.feature{left:80px;top:910px;font-size:40px;color:var(--ink);gap:18px}
.brand.feature .brand-mark{width:44px;height:44px}
.tool-title{right:75px;top:822px;width:600px;text-align:right;font-family:"Open Sans",sans-serif;font-size:39px;line-height:50px;color:var(--ink)}
.tool-hint{right:75px;top:1005px;font-family:"Open Sans",sans-serif;font-style:italic;font-size:16px;color:#444}
.field-group{display:flex;height:42px;width:287px;border-radius:21px;overflow:hidden;background:var(--field)}
.field-group .field{flex:1;padding-left:23px;display:flex;align-items:center;font-size:14.5px;color:#666}
.field-group .submit{width:108px;background:var(--orange);color:var(--white);font-size:14.5px;display:flex;align-items:center;justify-content:center;clip-path:polygon(0 0,100% 0,100% 100%,20px 100%);padding-left:16px}
.postcode{left:838px;top:1047px}
.band-title{left:75px;top:1340px;font-family:"Roboto Condensed",sans-serif;font-size:37px;line-height:48px;color:var(--white);text-transform:uppercase}
.btn.band-cta{left:75px;top:1538px;width:290px;height:54px;font-size:17px}
.dot{width:11px;height:11px;border-radius:50%;background:#e6e6e6;left:1111px}
.dot.active{width:22px;height:22px;left:1105px;background:none;border:2px solid #e6e6e6}
.dot.active::after{content:"";position:absolute;left:4px;top:4px;width:10px;height:10px;border-radius:50%;background:#e6e6e6}
.foot-heading{top:1848px;font-size:36px;font-weight:400;color:var(--ink)}
.facts{left:75px;top:1917px;list-style:none;font-size:15.5px;color:var(--muted);line-height:20px;width:360px}
.facts li{position:relative;padding-left:26px;margin-bottom:21px}
.facts li::before{content:"";position:absolute;left:0;top:3px;width:14px;height:14px;border-radius:50%;background:var(--orange);clip-path:polygon(0 0,60% 0,100% 50%,60% 100%,0 100%)}
.social{top:1922px;width:36px;height:36px;border-radius:50%}
.newsletter{left:838px;top:1923px;height:40px}
.legal{right:78px;top:2082px;display:flex;gap:22px;font-size:16px;font-weight:500;color:var(--ink)}
.to-top{left:1071px;top:2152px;width:54px;height:54px;border-radius:50%;background:var(--orange)}
.foot-band{left:0;top:2189px;width:1200px;height:87px;background:var(--orange);clip-path:polygon(0 0,100% 33px,100% 100%,0 100%)}
.copyright{left:75px;top:2228px;font-size:13.5px;color:var(--white)}
</style>
</head>
<body>
<div class="hero-photo" role="img" aria-label="Skyline of city office towers against a pale sky"></div>

<div class="brand header abs"><span class="brand-mark"></span>CORVANE HOLLIS</div>
<div class="nav abs" style="left:616px">PROPERTY SEARCH</div>
<div class="nav abs" style="left:761px">DISCOVER</div>
<div class="nav abs" style="left:850px">ABOUT ˅</div>
<div class="pill login abs">LOGIN</div>
<div class="pill register abs">REGISTER</div>

<h1 class="hero-title abs">Do you think<br>your business rates<br>are too high?</h1>
<p class="hero-text abs">Use our free valuation tool below or book a valuation with one of our qualified surveyors.No shock commissions and fair fixed fees from £295!</p>
<div class="btn hero-cta abs">Register now</div>

<div class="brand feature abs"><span class="brand-mark"></span>CORVANE HOLLIS</div>
<h2 class="tool-title abs" style="font-weight:400">Use our free valuation<br>tool to get an instant<br>estimate of your rateable value.</h2>
<p class="tool-hint abs">Enter your commercial property postcode to begin the valuation process!</p>
<div class="field-group postcode abs"><span class="field">Enter Postcode...</span><span class="submit">SUBMIT</span></div>

<div class="band-photo" role="img" aria-label="Black and white view up a glass office tower facade"></div>
<h2 class="band-title abs" style="font-weight:400">Book a qualified surveyor<br>to estimate your property's<br>rateable value</h2>
<div class="btn band-cta abs">Book valuation now</div>
<span class="dot abs" style="top:1469px"></span>
<span class="dot active abs" style="top:1495px"></span>
<span class="dot abs" style="top:1533px"></span>

<h3 class="foot-heading abs" style="left:75px">Find Out More</h3>
<ul class="facts abs">
  <li>Company Registration Number: 10473385</li>
  <li>Company Registered Address: Harrow Point, Quayside Park, Manchester M50 4QL</li>
</ul>

<h3 class="foot-heading abs" style="left:523px">Follow Us</h3>
<span class="social abs" style="left:504px;background:#3b5a98" aria-label="Social profile one"></span>
<span class="social abs" style="left:556px;background:#1a6fa0" aria-label="Social profile two"></span>
<span class="social abs" style="left:608px;background:#28a7dd" aria-label="Social profile three"></span>
<span class="social abs" style="left:658px;background:#b0306f" aria-label="Social profile four"></span>

<h3 class="foot-heading abs" style="right:80px">Newsletter</h3>
<div class="field-group newsletter abs"><span class="field">Enter Email...</span><span class="submit">SUBMIT</span></div>

<nav class="legal abs"><span>PRICING PLANS</span><span>FAQS</span><span>CONTACT</span><span>LEGAL &amp; TERMS</span></nav>

<div class="to-top abs">
  <svg width="54" height="54" viewBox="0 0 54 54" aria-label="Back to top"><path d="M27 13 L37 26 H31 V40 H23 V26 H17 Z" fill="#fff"/></svg>
</div>

<div class="foot-band abs"></div>
<p class="copyright abs">© 2019 All Rights Reserved.</p>
</body>
</html>
```